Corporate Letterhead

Looking for a new corporate letterhead design. Our colors are orange and gray.

We'd like it if the below could be included somehow in the letterhead.                                       

Partnerships | Results | Quality

• Logo, Company Name, Address, Phone #, Fax #, Web address, Email address (optional), the phrase "A Service Disable Veteran Owned Small Business".

```html
<!DOCTYPE html>
<html lang="en">
<head>
<meta charset="utf-8">
<title>Veridian Systems, Inc — Letterhead</title>
<link rel="stylesheet" href="https://fonts.googleapis.com/css2?family=Questrial&display=swap">
<style>
  :root {
    --backdrop: #dcdcdc;
    --paper: #ffffff;
    --brand-orange: #e3821f;
    --brand-gray: #8a8d96;
    --text-gray: #5f6068;
    --ink-dark: #3b3c42;
  }
  * { margin: 0; padding: 0; box-sizing: border-box; }
  html, body {
    width: 1200px; height: 968px; overflow: hidden;
    background: var(--backdrop);
    font-family: "Questrial", "Century Gothic", sans-serif;
  }
  .letterhead {
    position: absolute;
    left: 282px; top: 34px;
    width: 636px; height: 900px;
    background: var(--paper);
    box-shadow: 0 6px 22px rgba(0,0,0,0.12);
  }
  .brand {
    position: absolute; left: 44px; top: 44px;
    display: flex; align-items: center; gap: 10px;
  }
  .brand-dot {
    width: 26px; height: 26px; border-radius: 50%;
    background: var(--brand-orange);
  }
  .brand-name {
    color: var(--brand-orange);
    font-size: 22px; letter-spacing: 1px; line-height: 1.05;
  }
  .tagline {
    position: absolute; right: 44px; top: 92px;
    font-size: 11px; letter-spacing: 1.4px;
    color: var(--text-gray);
  }
  .tagline .divider { color: var(--brand-orange); margin: 0 6px; }
  .contact {
    position: absolute; left: 170px; bottom: 38px;
    display: flex; gap: 34px;
    font-size: 10px; line-height: 1.55; color: var(--ink-dark);
  }
  .contact-group { display: flex; flex-direction: column; }
  .contact-line { display: flex; align-items: center; gap: 6px; }
  .contact-line svg { width: 10px; height: 10px; flex: none; }
  .footer-band {
    position: absolute; left: 0; bottom: 0;
    width: 636px; height: 22px;
  }
</style>
</head>
<body>
  <main class="letterhead">
    <header>
      <div class="brand">
        <span class="brand-dot"></span>
        <span class="brand-name">VERIDIAN SYSTEMS, INC</span>
      </div>
      <p class="tagline">PARTNERSHIPS<span class="divider">|</span>RESULTS<span class="divider">|</span>QUALITY</p>
    </header>

    <footer>
      <address class="contact">
        <div class="contact-group">
          <span>48 Harbour Lane</span>
          <span>London, E9 4QT</span>
        </div>
        <div class="contact-group">
          <span class="contact-line">
            <svg viewBox="0 0 10 10"><circle cx="5" cy="5" r="5" fill="var(--brand-orange)"/><path d="M3.2 2.6 L4.2 2.6 L4.5 3.8 L3.9 4.3 Q4.6 5.6 5.8 6.1 L6.3 5.5 L7.4 5.8 L7.4 6.8 Q5.4 7.2 3.8 5.5 Q2.8 4.2 3.2 2.6Z" fill="#fff"/></svg>
            020 7946 0321
          </span>
          <span class="contact-line">
            <svg viewBox="0 0 10 10"><circle cx="5" cy="5" r="5" fill="var(--brand-orange)"/><rect x="2.6" y="4" width="4.8" height="2.6" fill="#fff"/><rect x="3.4" y="2.4" width="3.2" height="1.4" fill="#fff"/></svg>
            020 7946 0322
          </span>
        </div>
        <div class="contact-group">
          <span class="contact-line">
            <svg viewBox="0 0 10 10"><circle cx="5" cy="5" r="5" fill="var(--brand-orange)"/><rect x="2.5" y="3.2" width="5" height="3.6" fill="#fff"/><path d="M2.5 3.2 L5 5.2 L7.5 3.2" fill="none" stroke="var(--brand-orange)" stroke-width="0.6"/></svg>
            hello@veridiansys.com
          </span>
          <span class="contact-line">
            <svg viewBox="0 0 10 10"><circle cx="5" cy="5" r="5" fill="var(--brand-orange)"/><circle cx="5" cy="5" r="2.6" fill="none" stroke="#fff" stroke-width="0.7"/><path d="M2.4 5 H7.6 M5 2.4 V7.6" stroke="#fff" stroke-width="0.6"/></svg>
            www.veridiansys.com
          </span>
        </div>
      </address>
      <svg class="footer-band" viewBox="0 0 636 22" preserveAspectRatio="none" aria-hidden="true">
        <polygon points="0,0 188,0 172,22 0,22" fill="var(--brand-gray)"/>
        <polygon points="196,0 636,0 636,22 180,22" fill="var(--brand-orange)"/>
      </svg>
    </footer>
  </main>
</body>
</html>
```